Flyer-Design für feldwinkel.de
Zielgruppe
Wir vertreiben im Versandhandel über www.feldwinkel.de Pflanztöpfe/Schalen mit Selbstbewässerung. Der Hauptfokus liegt hier auf Grabschalen / Grabvasen
Aufgabenstellung
Flyer bitte im Format DIN-Lang.
Der Flyer soll sehr Bildhaft sein mit wenig Text.
Weitere Grafiken / Texte erhalten sie auch im Onlineshop www.feldwinkel.de

```html
<!DOCTYPE html>
<html lang="de">
<head>
<meta charset="utf-8">
<title>Flyer feldwinkel.de</title>
<link href="https://fonts.googleapis.com/css2?family=Exo+2:wght@400;600;700&display=swap" rel="stylesheet">
<style>
  :root {
    --green: #9cba1f;
    --green-line: #c3d36a;
    --black: #161616;
    --white: #ffffff;
    --paper: #f7f7f5;
    --grey-text: #8c8c8c;
    --frame-grey: #cdcdcd;
    --stage: #e9e7e2;
    --ink: #1c1c1c;
  }
  * { box-sizing: border-box; margin: 0; padding: 0; }
  html, body { width: 1200px; height: 750px; overflow: hidden; }
  body { background: var(--stage); font-family: "Exo 2", sans-serif; position: relative; }

  .flyer { position: absolute; top: 25px; width: 330px; height: 700px; overflow: hidden; }
  .flyer--front { left: 250px; background: var(--black); }
  .flyer--back { left: 620px; background: var(--paper); }

  .photo { position: absolute; }
  .price { position: absolute; font-weight: 600; font-size: 24px; letter-spacing: 0.5px; line-height: 1; white-space: nowrap; }
  .caption { position: absolute; font-size: 9px; line-height: 1.3; letter-spacing: 0.7px; white-space: nowrap; }
  .on-photo { color: var(--white); text-shadow: 0 1px 3px rgba(0,0,0,0.45); }
  .on-paper { color: var(--ink); }
  .on-paper.price { font-weight: 700; }
  .on-paper.caption { font-weight: 700; }

  /* front side */
  .photo--grave {
    left: 0; top: 0; width: 330px; height: 250px;
    background:
      linear-gradient(180deg, rgba(0,0,0,0.25) 0%, rgba(0,0,0,0) 22%),
      linear-gradient(180deg, #a9c3d6 0%, #9cb98a 14%, #5f8a3a 30%, #7a9d4c 44%, #c0a56b 52%, #b7b7b2 62%, #d8d8d4 76%, #9b9b97 100%);
  }
  .photo--terrace {
    left: 0; top: 250px; width: 330px; height: 190px;
    background:
      linear-gradient(180deg, rgba(0,0,0,0) 55%, rgba(0,0,0,0.4) 100%),
      linear-gradient(180deg, #6f8f49 0%, #d9dbdc 18%, #a9b4bc 40%, #8a8f92 58%, #6d6a64 78%, #55524d 100%);
  }
  .identity { position: absolute; left: 0; top: 440px; width: 330px; height: 260px; padding: 30px 26px; }
  .brand { display: flex; align-items: center; gap: 10px; }
  .brand-square { width: 14px; height: 14px; background: var(--green); }
  .brand-name { color: var(--green); font-weight: 700; font-size: 36px; line-height: 1; }
  .tagline { margin-top: 24px; color: var(--grey-text); font-size: 12px; line-height: 1.4; letter-spacing: 0.7px; }
  .contact { margin-top: 22px; list-style: none; color: var(--green); font-size: 13px; line-height: 1.6; letter-spacing: 0.5px; }
  .contact li { display: flex; align-items: center; gap: 7px; }
  .contact svg { width: 11px; height: 11px; flex: none; }

  /* back side */
  .photo--herbs {
    left: 14px; top: 14px; width: 148px; height: 168px;
    background:
      linear-gradient(180deg, rgba(0,0,0,0.18) 0%, rgba(0,0,0,0) 30%),
      linear-gradient(180deg, #86b24a 0%, #a9c86e 22%, #c6d957 40%, #e6eadc 58%, #f3f3f0 78%, #dededa 100%);
  }
  .photo--orchid {
    left: 170px; top: 40px; width: 146px; height: 190px;
    background:
      linear-gradient(180deg, rgba(0,0,0,0) 55%, rgba(0,0,0,0.35) 100%),
      linear-gradient(180deg, #f4f0ed 0%, #ede4e4 30%, #c9729f 42%, #f2efea 54%, #c8b3a4 72%, #5c4b44 100%);
  }
  .frame--grey { position: absolute; left: 14px; top: 248px; width: 302px; height: 196px; border: 2px solid var(--frame-grey); }
  .photo--box {
    left: 10px; top: 10px; width: 230px; height: 128px;
    background: linear-gradient(180deg, #f3eef1 0%, #efe4ea 25%, #d63b48 48%, #c24b5a 60%, #9f84c8 78%, #c7b6e0 100%);
  }
  .frame--green { position: absolute; left: 14px; top: 466px; width: 302px; height: 196px; border: 2px solid var(--green-line); border-left: none; }
  .photo--plant {
    left: 14px; top: 430px; width: 152px; height: 230px; border-radius: 6px;
    background: linear-gradient(180deg, #eef2d8 0%, #4f7a33 22%, #2f5a25 45%, #5b7f36 62%, #c8d94a 76%, #f1f1ee 88%, #e4e4e0 100%);
  }
  .web { position: absolute; left: 0; bottom: 16px; width: 330px; text-align: center; color: var(--green); font-weight: 600; font-size: 14px; letter-spacing: 0.7px; }
</style>
</head>
<body>

<section class="flyer flyer--front" aria-label="Flyer Vorderseite">
  <div class="photo photo--grave" role="img" aria-label="Foto: Grabschale mit Heide und Grabvase mit roten Rosen auf einem Grab im Garten"></div>
  <span class="price on-photo" style="left:22px; top:18px;">19,90 €</span>
  <span class="caption on-photo" style="left:22px; top:46px;">Grabschale mit Wasserspeicher</span>
  <span class="price on-photo" style="left:214px; top:190px;">12,90 €</span>
  <span class="caption on-photo" style="left:214px; top:218px;">Grabvase</span>

  <div class="photo photo--terrace" role="img" aria-label="Foto: weißer Bewässerungskasten mit Lavendel auf einer Holzterrasse vor Lounge-Möbeln"></div>
  <span class="price on-photo" style="left:22px; top:380px;">36,90 €</span>
  <span class="caption on-photo" style="left:22px; top:408px;">Bewässerungskasten<br>Terrasse 40 mit Rollen</span>

  <div class="identity">
    <div class="brand">
      <span class="brand-square"></span>
      <span class="brand-name">feldwinkel</span>
    </div>
    <p class="tagline">feldwinkel.de Ihr Onlineshop für<br>Selbstbewässerung.</p>
    <ul class="contact">
      <li>
        <svg viewBox="0 0 12 12" aria-hidden="true"><path d="M3 1l2 2.5-1.2 1.2a7 7 0 0 0 3.5 3.5L8.5 7 11 9l-1.2 2A9 9 0 0 1 1 2.2z" fill="currentColor"/></svg>
        01234 56789
      </li>
      <li>info@feldwinkel-versand.de</li>
      <li>www.feldwinkel.de</li>
    </ul>
  </div>
</section>

<section class="flyer flyer--back" aria-label="Flyer Rückseite">
  <div class="photo photo--herbs" role="img" aria-label="Foto: grüner Bewässerungstopf mit Kräutern auf einem Küchentisch mit Gemüse"></div>
  <span class="price on-photo" style="left:24px; top:24px;">3,49 €</span>
  <span class="caption on-photo" style="left:24px; top:51px;">Bewässerungstopf<br>SALVIA für Kräuter</span>

  <div class="photo photo--orchid" role="img" aria-label="Foto: weißer Bewässerungstopf mit pinker Orchidee in einem hellen Wohnraum"></div>
  <span class="price on-photo" style="left:178px; top:172px;">16,90 €</span>
  <span class="caption on-photo" style="left:178px; top:199px;">Bewässerungstopf<br>LUMIA für Orchideen</span>

  <div class="frame--grey">
    <div class="photo photo--box" role="img" aria-label="Foto: lila Bewässerungskasten mit roten Blüten neben pinker Gießflasche"></div>
    <span class="price on-paper" style="left:186px; top:144px;">9,90 €</span>
    <span class="caption on-paper" style="left:158px; top:168px;">Bewässerungskasten<br>DUETTO</span>
  </div>

  <div class="frame--green"></div>
  <div class="photo photo--plant" role="img" aria-label="Foto: weiß-grüner Bewässerungstopf mit Christrose und Efeu"></div>
  <span class="price on-paper" style="left:186px; top:540px;">7,90 €</span>
  <span class="caption on-paper" style="left:180px; top:566px;">Bewässerungstopf DUETTO</span>

  <p class="web">www.feldwinkel.de</p>
</section>

</body>
</html>
```